Card Design to Advertise New Business

I am looking to have a card designed so that I can pass it out to help promote my business. I have never done this before so I honestly do not know where to start with any ideas. I am providing my website address to help. I provide math tutoring, test prep, and schooling options.

I am looking for a card bigger than a business card but smaller than a flyer. Something front and back that I can pass out.

Business Information
Phone: 470-526-1984
Website: www.brightmaplestudyhub.com
Address: 418 Larkwood Rd Ste 210 Marietta GA 30068
Email: brightmapleservices@kestrelpostmail.com

Services:
Math Tutoring
SAT & ACT Test Prep
Group and Private Sessions
Fully Accredited Private School

Target Market(s)

Middle and High School Students

Industry/Entity Type

Education

Requirements
Must have
• Information from my website

```html
<!DOCTYPE html>
<html lang="en">
<head>
<meta charset="utf-8">
<title>Bright Maple Study Hub – Postcard</title>
<link href="https://fonts.googleapis.com/css2?family=Barlow:wght@400;500;600&family=Barlow+Condensed:wght@500;600;700&family=Sriracha&family=Dancing+Script:wght@600&display=swap" rel="stylesheet">
<style>
  :root{
    --stage:#333333;
    --white:#ffffff;
    --blue-top:#3b5fc9;
    --blue-bottom:#1aa6e4;
    --purple:#6a3fb0;
    --green:#5cc23a;
    --green-dark:#48a92c;
    --red:#c8321b;
    --navy:#0d1b6e;
    --yellow:#f7e11c;
    --brand-blue:#2f5fbf;
    --sky:#2a9ad6;
  }
  *{box-sizing:border-box;margin:0;padding:0}
  html,body{width:1200px;height:1177px;overflow:hidden;background:var(--stage)}
  .card{position:absolute;background:var(--white);overflow:hidden;font-family:"Barlow",sans-serif;color:var(--white)}
  .card--front{left:266px;top:75px;width:755px;height:500px}
  .card--back{left:265px;top:604px;width:755px;height:503px}
  .abs{position:absolute}
  .shapes{position:absolute;left:0;top:0}
  .photo{position:absolute}
  .photo--round{border-radius:50%;border:6px solid var(--white)}
  .front-title{left:350px;width:460px;top:14px;text-align:center;font-family:"Barlow Condensed",sans-serif;font-weight:600;font-size:38px;line-height:37px;letter-spacing:.3px}
  .front-tagline{left:350px;width:460px;top:92px;text-align:center;font-family:"Sriracha",cursive;font-size:30px;color:var(--yellow)}
  .front-intro{left:435px;width:304px;top:141px;font-size:12.6px;line-height:16.3px;text-align:justify;letter-spacing:.2px}
  .enrolling{left:420px;width:300px;top:258px;text-align:center;font-family:"Sriracha",cursive;font-size:31px;color:var(--yellow);transform:rotate(-3deg)}
  .offer{display:flex;align-items:center;gap:10px;font-family:"Barlow",sans-serif;font-weight:600;font-size:11px;line-height:12.5px;text-transform:uppercase}
  .offer svg{flex:none}
  .credit{left:429px;top:434px;font-size:6px;font-style:italic;opacity:.9}
  .brand{text-align:center;font-family:"Barlow Condensed",sans-serif;font-weight:700;color:var(--brand-blue);font-size:27px;line-height:25px}
  .brand-dot{border-radius:50%;background:var(--brand-blue)}
  .phone-box{display:flex;align-items:center;justify-content:center;gap:12px;background:var(--red);font-family:"Barlow Condensed",sans-serif;font-weight:600;font-size:29px;color:var(--white)}
  .contact{display:flex;align-items:flex-start;gap:6px;font-size:11.5px;line-height:14px;font-weight:500}
  .contact svg{flex:none;margin-top:2px}
  .contact strong{font-weight:600}
  .back-head{left:15px;top:10px;font-family:"Barlow Condensed",sans-serif;font-weight:600;font-size:27px;line-height:31px}
  .back-head .blue{color:var(--brand-blue)}
  .back-head .purple{color:var(--purple)}
  .back-head .red{color:var(--red)}
  .stamp{left:640px;top:21px;width:88px;height:103px;border:1px solid #9a9a9a}
  .services-title{left:17px;top:96px;font-family:"Dancing Script",cursive;font-weight:600;font-size:32px}
  .price{left:-4px;width:80px;height:64px;border:2px solid var(--white);border-radius:0 10px 10px 0;text-align:center;line-height:1}
  .price small{display:block;font-size:11px;padding-top:6px}
  .price b{display:block;font-family:"Barlow Condensed",sans-serif;font-weight:600;font-size:25px;margin:1px 0}
  .price--purple{background:var(--purple)}
  .price--red{background:var(--red)}
  .price--blue{background:var(--sky)}
  .service-name{left:95px;font-size:19.5px;font-weight:500;letter-spacing:.4px;line-height:21px;text-transform:uppercase}
  .more{left:15px;top:407px;font-size:17px;font-weight:500}
</style>
</head>
<body>

<!-- FRONT -->
<section class="card card--front">
  <div class="photo" role="img" aria-label="Photo of a smiling student working at a desk with a tutor beside him" style="left:0;top:0;width:460px;height:330px;background:linear-gradient(180deg,#c9d3df 0%,#e8edf2 55%,#ffffff 100%)"></div>

  <svg class="shapes" width="755" height="500" viewBox="0 0 755 500" aria-hidden="true">
    <defs>
      <linearGradient id="panelBlue" x1="0" y1="0" x2="0" y2="1">
        <stop offset="0" stop-color="#3b5fc9"/>
        <stop offset="1" stop-color="#1aa6e4"/>
      </linearGradient>
    </defs>
    <path d="M278,0 H755 V252 C630,258 500,276 410,302 C360,210 330,70 278,0 Z" fill="url(#panelBlue)" stroke="#ffffff" stroke-width="5"/>
    <path d="M395,306 C490,280 630,260 755,254 V453 H395 Z" fill="#6a3fb0" stroke="#ffffff" stroke-width="5"/>
    <rect x="0" y="453" width="755" height="47" fill="#5cc23a"/>
  </svg>

  <div class="photo photo--round" role="img" aria-label="Photo of a young child writing in a notebook" style="left:246px;top:256px;width:160px;height:160px;background:radial-gradient(circle at 40% 40%,#f1d8c4,#c98e6c 70%,#b04b3a)"></div>

  <div class="abs brand-dot" style="left:94px;top:280px;width:90px;height:90px"></div>
  <div class="abs brand" style="left:10px;top:378px;width:260px">BRIGHT MAPLE<br>STUDY HUB</div>

  <div class="abs front-title">PATH COACHING<br>AND MATH TUTORING</div>
  <div class="abs front-tagline">For All Ages</div>
  <p class="abs front-intro">Our goal is to not only build math competency but build self-confidence to perform better in classes and tests and any other paths you choose to take in life. We will work to heighten creativity, improve concentration, lower stress, and increase self-awareness.</p>
  <div class="abs enrolling">Now Enrolling!</div>

  <div class="abs offer" style="left:428px;top:320px">
    <svg width="40" height="40" viewBox="0 0 40 40" fill="none" stroke="#fff" stroke-width="1.8"><rect x="2" y="2" width="36" height="36" rx="3"/><path d="M20 2V38M2 20H38M8 11H15M11.5 7.5V14.5M25 11H32M8 29H15M25 27H32M25 31H32M9 25L14 33M14 25L9 33"/></svg>
    <span>Math<br>Tutoring</span>
  </div>
  <div class="abs offer" style="left:556px;top:322px">
    <svg width="58" height="34" viewBox="0 0 58 34" fill="none" stroke="#fff" stroke-width="1.8"><circle cx="9" cy="10" r="4"/><circle cx="18" cy="7" r="4.5"/><circle cx="27" cy="10" r="4"/><path d="M2 28V20Q9 15 14 18M34 28V20Q27 15 22 18M11 30V19Q18 13 25 19V30Z"/><circle cx="49" cy="8" r="5"/><path d="M41 30V22Q49 14 57 22V30Z"/></svg>
    <span>Group and<br>Private Sessions</span>
  </div>
  <div class="abs offer" style="left:428px;top:378px">
    <svg width="40" height="44" viewBox="0 0 40 44" fill="none" stroke="#fff" stroke-width="1.8"><rect x="3" y="2" width="26" height="40" rx="2"/><path d="M8 8H24M8 16H12M15 16H24M8 24H12M15 24H24M8 32H12M15 32H20M36 10L24 38L22 42L26 39L38 11Z"/></svg>
    <span>SAT &amp; ACT<br>Test Prep</span>
  </div>
  <div class="abs offer" style="left:582px;top:376px">
    <svg width="34" height="48" viewBox="0 0 34 48" fill="none" stroke="#fff" stroke-width="1.8"><circle cx="17" cy="17" r="14"/><circle cx="17" cy="17" r="9"/><path d="M17 11L19 15.5L23.5 16L20 19L21 23.5L17 21L13 23.5L14 19L10.5 16L15 15.5Z"/><path d="M9 29L5 44L11 41L14 46L17 31M25 29L29 44L23 41L20 46L17 31"/></svg>
    <span>Fully Accredited<br>Private School</span>
  </div>
  <div class="abs credit">Icons by Linewise, Dotcraft, Tidy Glyph from Iconharbor.com</div>

  <div class="abs phone-box" style="left:21px;top:444px;width:217px;height:56px;border-radius:8px 8px 0 0">
    <svg width="28" height="28" viewBox="0 0 28 28" aria-hidden="true"><circle cx="14" cy="14" r="12.5" fill="none" stroke="#fff" stroke-width="2.4"/><path d="M9 7.5L11.5 7L13 11L11.5 12.5Q13 16 15.5 17L17 15.5L21 17L20.5 19.5Q18 22 14 19.5Q9 16 7.5 12Q6.8 9 9 7.5Z" fill="#fff"/></svg>
    <span>470-526-1984</span>
  </div>
  <div class="abs contact" style="left:316px;top:462px">
    <svg width="9" height="12" viewBox="0 0 9 12"><path d="M4.5 0A4.5 4.5 0 0 0 0 4.5C0 8 4.5 12 4.5 12S9 8 9 4.5A4.5 4.5 0 0 0 4.5 0Z" fill="#f7e11c"/><circle cx="4.5" cy="4.5" r="1.7" fill="#5cc23a"/></svg>
    <span>418 Larkwood Rd Ste 210<br>Marietta GA 30068</span>
  </div>
  <div class="abs contact" style="left:516px;top:462px;font-size:11px">
    <svg width="10" height="24" viewBox="0 0 10 24"><rect x="0" y="1" width="10" height="7" fill="#f7e11c"/><path d="M0 1L5 5L10 1" stroke="#5cc23a" fill="none"/><circle cx="5" cy="19" r="4.5" fill="#f7e11c"/><path d="M0.5 19H9.5M5 14.5V23.5" stroke="#5cc23a"/></svg>
    <span>brightmapleservices@kestrelpostmail.com<br><strong>www.brightmaplestudyhub.com</strong></span>
  </div>
</section>

<!-- BACK -->
<section class="card card--back">
  <svg class="shapes" width="755" height="503" viewBox="0 0 755 503" aria-hidden="true">
    <path d="M0,100 C180,80 320,88 400,150 C480,215 505,330 515,452 H0 Z" fill="#5cc23a"/>
    <path d="M60,452 C150,330 330,300 480,360" fill="none" stroke="#48a92c" stroke-width="2" opacity=".6"/>
    <rect x="0" y="452" width="755" height="51" fill="#0d1b6e"/>
    <rect x="516" y="452" width="239" height="51" fill="#c8321b"/>
  </svg>

  <div class="abs back-head">
    <div class="blue">MORE THAN JUST MATH TUTORING!</div>
    <div><span class="purple">WE ARE </span><span class="red">PATH COACHES</span></div>
  </div>
  <div class="abs stamp"></div>

  <div class="abs services-title">Services</div>

  <div class="abs price price--purple" style="top:168px"><small>Starting</small><b>$30</b><small style="padding:0">Per hour</small></div>
  <div class="abs service-name" style="top:190px">Group Sessions</div>
  <div class="abs price price--red" style="top:244px"><small>Starting</small><b>$50</b><small style="padding:0">Per hour</small></div>
  <div class="abs service-name" style="top:266px">Private Sessions</div>
  <div class="abs price price--blue" style="top:320px"><small>Starting</small><b>$100</b><small style="padding:0">Per month</small></div>
  <div class="abs service-name" style="top:333px">Online Courses<br>and Programs</div>
  <div class="abs more">More educational services available!</div>

  <div class="photo photo--round" role="img" aria-label="Photo of a teenage student holding books in front of a chalkboard" style="left:275px;top:76px;width:154px;height:154px;background:radial-gradient(circle at 50% 45%,#d9c2a6,#8a8f99 75%)"></div>
  <div class="photo photo--round" role="img" aria-label="Photo of a boy with a backpack writing on a green chalkboard" style="left:341px;top:205px;width:196px;height:196px;background:radial-gradient(circle at 40% 55%,#8fb0c8,#2f5b4a 75%)"></div>

  <div class="abs brand-dot" style="left:593px;top:282px;width:90px;height:90px"></div>
  <div class="abs brand" style="left:508px;top:380px;width:260px">BRIGHT MAPLE<br>STUDY HUB</div>

  <div class="abs contact" style="left:17px;top:462px">
    <svg width="9" height="12" viewBox="0 0 9 12"><path d="M4.5 0A4.5 4.5 0 0 0 0 4.5C0 8 4.5 12 4.5 12S9 8 9 4.5A4.5 4.5 0 0 0 4.5 0Z" fill="#f7e11c"/><circle cx="4.5" cy="4.5" r="1.7" fill="#0d1b6e"/></svg>
    <span>418 Larkwood Rd Ste 210<br>Marietta GA 30068</span>
  </div>
  <div class="abs contact" style="left:230px;top:462px;font-size:11px">
    <svg width="10" height="24" viewBox="0 0 10 24"><rect x="0" y="1" width="10" height="7" fill="#f7e11c"/><path d="M0 1L5 5L10 1" stroke="#0d1b6e" fill="none"/><circle cx="5" cy="19" r="4.5" fill="#f7e11c"/><path d="M0.5 19H9.5M5 14.5V23.5" stroke="#0d1b6e"/></svg>
    <span>brightmapleservices@kestrelpostmail.com<br><strong>www.brightmaplestudyhub.com</strong></span>
  </div>
  <div class="abs phone-box" style="left:516px;top:452px;width:239px;height:51px">
    <svg width="28" height="28" viewBox="0 0 28 28" aria-hidden="true"><circle cx="14" cy="14" r="12.5" fill="none" stroke="#fff" stroke-width="2.4"/><path d="M9 7.5L11.5 7L13 11L11.5 12.5Q13 16 15.5 17L17 15.5L21 17L20.5 19.5Q18 22 14 19.5Q9 16 7.5 12Q6.8 9 9 7.5Z" fill="#fff"/></svg>
    <span>470-526-1984</span>
  </div>
</section>

</body>
</html>
```